Financial investment calculator report for real estae - layout & design

I am looking to Create a web report utilizing the attached information. It is an investment calculator report that will be customized report based on an online calculator. Therefore the report will need to be designed in a manner that a backend developer will be able to build off of.

The report will need to be web based but also printed in PDF format. The report will need to include the calculation format as well as be templeted to add a report user unique profile information like Headshot, Business Logo, Name, Telephone number, email etc.

The report should be modern and clean and easy to read and use a modern clean template design. It should be able to be easily color customized by the end user to produce templets in Red, Blue, Green, and Greyscale.

The report should be no more than 3 pages total with out breaking up the sections.

Section One - Cover sheet including agent bio info, Report Title and property address (both prominent), 400 Character space for property description, Property Pictures (3), and a google Maps integration image showing property location, It should also have room for about 100 words for a text disclaimer. (I will provide text soon)

Section Two - Inputs from the calculator

Section 3 - The Four Benefits & Rates of Return

Once I have a completed/approved form I will have about a half dozen forms/reports that will need to be laid out with a similar aesthetic.

Feel free to ask me any questions. Thank You
Tobin
Updates

Target Market(s)

This report will be produced by real estate agents forvtheir investor clients. It should denote professionalism

Font styles to use
Sans Serif

Colors
0054AA
0677BA
7BADD7
CADEEF
E8F1F8
00AB8E
00BBA5
67D7C9
C6EFE9
E9F9F6
EB3D1F
EC4F4E
F09395
F8D3D4
FCEDEE

```html
<!DOCTYPE html>
<html lang="en">
<head>
<meta charset="utf-8">
<title>Investment Analysis – 412 Fairhaven</title>
<link href="https://fonts.googleapis.com/css2?family=Work+Sans:wght@400;500;600;700&display=swap" rel="stylesheet">
<style>
  :root{
    --brand:#a8201f;
    --ink:#3a3a3a;
    --text:#2b2b2b;
    --muted:#6b6b6b;
    --band:#e8e8e8;
    --card:#e6e6e6;
    --page:#ffffff;
  }
  *{box-sizing:border-box;margin:0;padding:0}
  html,body{width:929px;height:1200px;overflow:hidden;background:var(--page)}
  body{font-family:"Work Sans",Arial,sans-serif;color:var(--text);position:relative}
  .print-meta{position:absolute;left:0;right:0;display:flex;justify-content:space-between;padding:0 14px;font-size:11px;color:#222}
  .print-meta.top{top:9px}
  .print-meta.bottom{top:1176px}
  .header-band{position:absolute;top:0;left:0;width:929px;height:205px;background:var(--band)}
  .brand{position:absolute;top:76px;left:0;width:929px;display:flex;justify-content:center;align-items:center;gap:14px}
  .brand-name{font-size:40px;font-weight:600;color:var(--brand);letter-spacing:3px}
  .report-title{position:absolute;top:270px;width:929px;text-align:center}
  .report-title h1{font-size:45px;font-weight:600;color:var(--ink);line-height:1.2}
  .report-title .address{font-size:45px;font-weight:700;color:var(--brand);line-height:1.2}
  .report-title .property-type{font-size:21px;font-weight:400;color:var(--brand);margin-top:6px}
  .photo{position:absolute;top:462px;height:197px;width:248px;border-radius:18px}
  .photo.exterior{left:79px;background:linear-gradient(180deg,#8a8fc4 0%,#c9a6c6 55%,#3d4664 100%)}
  .photo.kitchen{left:340px;background:linear-gradient(180deg,#f2f2f0 0%,#d9d6d1 55%,#7a5a40 100%)}
  .photo.galley{left:601px;background:linear-gradient(180deg,#efece6 0%,#d8d2c8 55%,#b9a58a 100%)}
  .about{position:absolute;left:88px;top:722px;width:330px}
  .about h2{font-size:12px;font-weight:500;letter-spacing:2.5px;color:var(--muted);margin-bottom:12px}
  .about p{font-size:15px;line-height:1.42;margin-bottom:30px}
  .map{position:absolute;left:455px;top:700px;width:393px;height:226px;border-radius:12px;background:linear-gradient(135deg,#f1f3f4 0%,#e7ebe9 60%,#dfe9e2 100%)}
  .card{position:absolute;top:988px;height:148px;background:var(--card);border-radius:16px}
  .agent-card{left:118px;width:302px}
  .headshot{position:absolute;left:77px;top:1004px;width:112px;height:112px;border-radius:50%;border:2px solid var(--brand);background:#fff;padding:5px}
  .headshot span{display:block;width:100%;height:100%;border-radius:50%;background:linear-gradient(180deg,#8f7f72 0%,#3c3f4a 100%)}
  .agent-info{position:absolute;left:228px;top:1018px;font-size:15px;line-height:1.5;color:var(--ink)}
  .agent-info .agent-name{font-weight:600}
  .disclaimer-card{left:436px;width:412px;padding:20px 20px}
  .disclaimer-card h3{font-size:14px;font-weight:600;margin-bottom:2px}
  .disclaimer-card p{font-size:13.5px;font-weight:500;line-height:1.5}
</style>
</head>
<body>
  <div class="header-band"></div>
  <div class="print-meta top"><span>5/30/23, 10:23 AM</span><span>Investment Analysis</span></div>

  <div class="brand">
    <svg width="44" height="44" viewBox="0 0 44 44" aria-hidden="true"><circle cx="22" cy="22" r="20" fill="none" stroke="var(--brand)" stroke-width="3"/></svg>
    <span class="brand-name">KEYSTONE REALTY</span>
  </div>

  <header class="report-title">
    <h1>Investment Analysis</h1>
    <div class="address">412 Fairhaven</div>
    <div class="property-type">15-Plex of 1bd/1bth Apartments</div>
  </header>

  <div class="photo exterior" role="img" aria-label="Property exterior photo at dusk"></div>
  <div class="photo kitchen" role="img" aria-label="Kitchen interior photo"></div>
  <div class="photo galley" role="img" aria-label="Second kitchen interior photo"></div>

  <section class="about">
    <h2>ABOUT THE PROPERTY</h2>
    <p>Lorem ipsum is a placeholder text commonly used to demonstrate the visual form of a document or a typeface without relying on meaningful content.</p>
    <p>Lorem ipsum is a placeholder text commonly used to demonstrate the visual form of a document or a typeface</p>
  </section>

  <div class="map" role="img" aria-label="Map showing the property location"></div>

  <div class="card agent-card"></div>
  <div class="headshot" role="img" aria-label="Agent headshot"><span></span></div>
  <div class="agent-info">
    <div class="agent-name">Greg Tobin</div>
    <div>admin1</div>
    <div>(555) 214-6037</div>
    <div>greg@keystonerealty.com</div>
  </div>

  <section class="card disclaimer-card">
    <h3>DISCLAIMER</h3>
    <p>In publishing and graphic design, Lorem ipsum is a placeholder text commonly used to demonstrate the visual form of a document or a typeface</p>
  </section>

  <div class="print-meta bottom"><span>https://www.propertyreports.com/report/pdf/5</span><span>1/3</span></div>
</body>
</html>
```